Verpackungsdesign einer Wassermatte in Baby-Blau gesucht
Zielgruppe
Wir verkaufen Kinder und Baby Produkte. Unsere Zielgruppe sind Eltern und deren Kinder.
Aufgabenstellung
- kindlich
- spielerisch
- mit Logo
- nicht zu bunt
- Hintergrundfarbe von der Verpackung Babyblau
- Maße der Verpackung sind anbei
- Das Produkt ist eine Wassermatte (Fotos anbei)

```html
<!DOCTYPE html>
<html lang="de">
<head>
<meta charset="utf-8">
<title>kiwora Wassermatte – Verpackung</title>
<link rel="stylesheet" href="https://fonts.googleapis.com/css2?family=Quicksand:wght@400;600;700&family=Kaushan+Script&family=Oswald:wght@600&display=swap">
<style>
  :root {
    --stage: #e4e3ea;
    --baby-blue: #dcecf3;
    --sky: #a9daf0;
    --sea: #5fb7e3;
    --deep-sea: #3a8fcb;
    --title-blue: #2f86cf;
    --ink: #3b3b3b;
    --alert-red: #d8213b;
    --white: #ffffff;
    --sun: #f6b72f;
  }
  * { box-sizing: border-box; margin: 0; padding: 0; }
  html, body { width: 1200px; height: 577px; overflow: hidden; }
  body {
    background: var(--stage);
    font-family: "Quicksand", sans-serif;
    color: var(--ink);
    display: flex;
    align-items: center;
    justify-content: center;
    gap: 22px;
  }
  .panel {
    position: relative;
    height: 400px;
    background: var(--baby-blue);
    overflow: hidden;
    box-shadow: 0 6px 18px rgba(60, 60, 90, .18);
  }
  .panel--front, .panel--back { width: 400px; }
  .panel--side { width: 120px; }

  .sea-band {
    position: absolute;
    left: 0; right: 0;
    background: linear-gradient(180deg, var(--sky), var(--sea));
  }
  .sea-scene {
    position: absolute;
    left: 0; right: 0; bottom: 0;
    background: linear-gradient(180deg, var(--sky) 0%, #8fcdec 55%, var(--sea) 100%);
  }

  .brand {
    position: absolute;
    display: flex;
    align-items: center;
    gap: 8px;
    font-weight: 600;
    color: var(--ink);
    letter-spacing: .5px;
  }
  .brand__dot {
    width: 34px; height: 34px;
    border-radius: 50%;
    background: var(--ink);
  }

  /* front */
  .panel--front .brand { top: 34px; left: 110px; font-size: 34px; }
  .panel--front .sea-band { top: 118px; height: 70px; opacity: .8; }
  .product-title {
    position: absolute;
    top: 122px; left: 0; right: 0;
    text-align: center;
    font-family: "Kaushan Script", cursive;
    font-size: 64px;
    color: var(--title-blue);
    transform: rotate(-12deg);
  }
  .panel--front .sea-scene { top: 215px; }
  .quality-badge {
    position: absolute;
    left: 28px; top: 228px;
    width: 120px; height: 120px;
  }
  .quality-badge__label {
    position: absolute;
    inset: 0;
    display: flex;
    align-items: center;
    justify-content: center;
    text-align: center;
    font-family: "Oswald", sans-serif;
    font-weight: 600;
    font-size: 17px;
    line-height: 1.05;
    color: var(--white);
    transform: rotate(-20deg);
  }

  /* side */
  .panel--side .sea-scene { top: 0; background: linear-gradient(180deg, var(--sea), var(--deep-sea) 60%, var(--sky)); }
  .panel--side .brand {
    top: 150px; left: -20px;
    font-size: 30px;
    transform: rotate(90deg);
  }

  /* back */
  .panel--back .sea-band { top: 150px; height: 90px; opacity: .7; }
  .panel--back .sea-scene { top: 250px; }
  .cert-marks {
    position: absolute;
    top: 24px; right: 30px;
    display: flex; flex-direction: column; gap: 14px; align-items: center;
  }
  .cert-mark { width: 34px; height: 28px; border-radius: 6px; background: var(--title-blue); }
  .cert-mark--round { border-radius: 50%; width: 34px; height: 34px; background: var(--sea); }
  .label-field {
    position: absolute;
    top: 22px; left: 40px;
    width: 110px; height: 62px;
    background: var(--white);
    border: 1px solid #c9cdd3;
  }
  .sender {
    position: absolute;
    top: 96px; right: 14px;
    font-size: 10px;
    line-height: 1.3;
    color: var(--ink);
    writing-mode: vertical-rl;
  }
  .steps {
    position: absolute;
    top: 96px; left: 28px;
    display: flex; gap: 18px;
  }
  .step { width: 130px; }
  .step__diagram {
    height: 78px;
    border: 2px solid var(--deep-sea);
    border-radius: 14px;
    background: rgba(255, 255, 255, .5);
    position: relative;
  }
  .step__number {
    position: absolute;
    right: -10px; bottom: -10px;
    width: 24px; height: 24px;
    border-radius: 50%;
    background: var(--deep-sea);
    color: var(--white);
    font-size: 12px; font-weight: 700;
    display: flex; align-items: center; justify-content: center;
  }
  .step__title { margin-top: 14px; font-size: 11px; font-weight: 700; color: var(--deep-sea); }
  .step__text { font-size: 10px; color: var(--deep-sea); line-height: 1.25; }
  .safety-note {
    position: absolute;
    top: 226px; left: 40px; right: 40px;
    padding: 12px 14px;
    border-radius: 12px;
    background: var(--alert-red);
    color: var(--white);
    font-size: 11.5px;
    font-weight: 700;
    line-height: 1.35;
    text-align: center;
    z-index: 1;
  }
</style>
</head>
<body>

  <section class="panel panel--front">
    <div class="brand"><span class="brand__dot"></span>kiwora</div>
    <div class="sea-band"></div>
    <h1 class="product-title">Wassermatte</h1>
    <div class="sea-scene" role="img" aria-label="Unterwasserszene mit gelbem U-Boot, Haien, Korallen und Luftblasen"></div>
    <div class="quality-badge">
      <svg viewBox="0 0 120 120" width="120" height="120" aria-hidden="true">
        <polygon fill="#d8213b" points="60,2 70,20 88,8 90,29 111,25 102,45 119,57 102,70 112,90 90,90 88,111 70,99 60,118 50,99 32,111 30,90 8,90 18,70 1,57 18,45 9,25 30,29 32,8 50,20"/>
      </svg>
      <div class="quality-badge__label">HOHE<br>QUALITÄT</div>
    </div>
  </section>

  <section class="panel panel--side">
    <div class="sea-scene" role="img" aria-label="Meereswellen mit Haien und Luftblasen"></div>
    <div class="brand"><span class="brand__dot"></span>kiwora</div>
  </section>

  <section class="panel panel--back">
    <div class="sea-band"></div>
    <div class="sea-scene" role="img" aria-label="Unterwasserszene mit gelbem U-Boot, Hai und Korallen"></div>
    <div class="label-field"></div>
    <div class="cert-marks">
      <span class="cert-mark"></span>
      <span class="cert-mark cert-mark--round"></span>
    </div>
    <p class="sender">Brandt &amp; Selle GbR<br>info@kiwora-store.de</p>
    <div class="steps">
      <div class="step">
        <div class="step__diagram" role="img" aria-label="Skizze der Wassermatte: Wasser einfüllen"><span class="step__number">1.</span></div>
        <p class="step__title">Erster Schritt</p>
        <p class="step__text">Wasser in den mittleren<br>Teil einfüllen</p>
      </div>
      <div class="step">
        <div class="step__diagram" role="img" aria-label="Skizze der Wassermatte: Luft in den Rand füllen"><span class="step__number">2.</span></div>
        <p class="step__title">Zweiter Schritt</p>
        <p class="step__text">Luft in den äußeren<br>Teil füllen</p>
      </div>
    </div>
    <p class="safety-note">Die Wassermatte darf nur unter Aufsicht eines Erwachsenen verwendet werden.<br>Geeignet für Kinder ab 3 Monaten.<br>Belastbar mit höchstens 40kg.</p>
  </section>

</body>
</html>
```